Business card design for engineering firm specializing in defense industry.

We need a professional business card design. Something simple but stands out. We are an engineering company specializing in composites in the defense industry.
Industry/Entity Type
Defense
Contact Information for Business Card
A simple black business card with the Varlonix yellow color is what we had in mind but open for other designs.
Colors
ffc214

```html
<!DOCTYPE html>
<html lang="en">
<head>
<meta charset="utf-8">
<title>Varlonix business card</title>
<link rel="stylesheet" href="https://fonts.googleapis.com/css2?family=Saira+Semi+Condensed:wght@400;700&display=swap">
<style>
  :root {
    --stage: #2b2d42;
    --card-white: #ffffff;
    --card-black: #0e0e0e;
    --ink: #111111;
    --paper-text: #f2f2f2;
    --accent: #ffc214;
  }
  * { box-sizing: border-box; margin: 0; padding: 0; }
  html, body {
    width: 1200px; height: 1000px; overflow: hidden;
    background: var(--stage);
    font-family: "Saira Semi Condensed", "Arial Narrow", sans-serif;
  }
  .stage { position: relative; width: 1200px; height: 1000px; }
  .card {
    position: absolute; width: 560px; height: 320px;
    box-shadow: 0 18px 40px rgba(0,0,0,0.35);
  }
  .card--front {
    left: 90px; top: 150px; background: var(--card-white);
    display: flex; align-items: center; justify-content: center; gap: 18px;
  }
  .brand-mark { width: 34px; height: 34px; background: var(--accent); }
  .brand-name {
    font-size: 64px; font-weight: 700; color: var(--ink); letter-spacing: 1px;
  }
  .card--back {
    left: 550px; top: 530px; background: var(--card-black);
    display: flex; align-items: center; justify-content: center;
    color: var(--paper-text);
  }
  .tagline {
    width: 200px; text-align: center; font-size: 21px; line-height: 1.35;
    letter-spacing: 0.5px;
  }
  .divider { width: 8px; height: 230px; margin: 0 28px; }
  .contact {
    width: 200px; font-size: 21px; line-height: 1.35; letter-spacing: 0.5px;
  }
</style>
</head>
<body>
  <main class="stage">
    <section class="card card--front" aria-label="Card front">
      <span class="brand-mark"></span>
      <h1 class="brand-name">Varlonix</h1>
    </section>
    <section class="card card--back" aria-label="Card back">
      <p class="tagline">Engineering<br>company<br>specializing in<br>composites<br>in the<br>defense industry</p>
      <svg class="divider" viewBox="0 0 8 230" aria-hidden="true">
        <polygon points="4,0 6,115 4,230 2,115" fill="#e6e6e6"/>
      </svg>
      <address class="contact" style="font-style:normal">
        Address<br>555 014 2790<br>info@varlonix.com<br>www.varlonix.com
      </address>
    </section>
  </main>
</body>
</html>
```